Web design for boutique law firm

Web design for law firm; practice areas include:
-international intellectual property counseling
-general corporate (contract negotiation, licensing, distribution agreements
-see my *very* outdated website at www.pvtlegalhouse.com: here is some of the home page content:

"PVT Law Group enjoys providing proactive, business-minded, efficient legal solutions for individuals and companies that benefit from major law firm experience at reasonable rates.

Some areas of emphasis include:

Counseling individuals and companies with respect to clearing, selecting, securing, managing, commercializing, and protecting intellectual property assets around the world. This includes traditional global brand management, marketing, advertising, and enforcement work as well as litigation.
PVT Law Group also provides general counseling services for individuals and businesses, from start-up advice to sophisticated business transactions strategy, agreement negotiating, dispute resolution, and litigation.
Before founding PVT Law Group in 2008, Curtis L. Abernathy led the Trademark, Copyright, & Brand Management Group for Falkner & Ingleby's Seattle office. Curtis was also a senior associate at Silicon Valley based Hartwell, Bexley, Oduya, & Penrose."

Target Market(s)

Clients/potential clients needing tier one, international intellectual property advice with "mega" law firm experience for much less than what we were/would be charging at the "mega firms".

Industry/Entity Type

Legal

Number of Pages Required

4 page

Font styles to use
Serif
Sans Serif

Colors

Designer to choose colors to be used in the design.

Requirements
Must have
• +Improvement over everything on current site at www.pvtlegalhouse.com.
• +Pictures/bios for me and my team (four of us right now).
• +Easy to update and add/remove content.
• +Must be superior in design (look, feel, ease of use, classy and elegant, but hip, reflects international practice).
• +i have logos and color schemes (see current website) but will consider improvements.
Nice to have
• Let me know your thoughts.
Should not have
• No cheese; no overt sales pitches or marketing (since law firm).

```html
<!DOCTYPE html>
<html lang="en">
<head>
<meta charset="utf-8">
<title>PVT Law Group PLLC</title>
<link rel="stylesheet" href="https://fonts.googleapis.com/css2?family=Open+Sans:wght@400;600;700&family=Montserrat:wght@400;500&family=Noto+Serif:wght@400&display=swap">
<style>
:root{
  --accent:#f26a21;
  --ink:#111111;
  --body:#2a2a2a;
  --footer-bg:#1e1e1e;
  --band:rgba(200,203,208,0.72);
  --header:rgba(236,240,244,0.78);
  --rule:#c9c9c9;
}
*{margin:0;padding:0;box-sizing:border-box}
html,body{width:1200px;height:1200px;overflow:hidden;background:#fff}
body{position:relative;font-family:"Open Sans",Arial,sans-serif;color:var(--body)}
.hero{position:absolute;left:0;top:0;width:1200px;height:534px;
  background:linear-gradient(180deg,#7f97b4 0%,#8fa3bb 18%,#b4a8a6 30%,#d9a07a 40%,#3c4a60 52%,#26303f 70%,#1a1f2a 100%)}
.site-header{position:absolute;left:0;top:0;width:1200px;height:66px;background:var(--header)}
.brand{position:absolute;left:217px;top:26px;font-family:"Montserrat",sans-serif;font-size:14px;letter-spacing:1px;color:var(--ink);display:flex;align-items:center;gap:7px}
.brand-mark{width:10px;height:10px;background:var(--accent)}
.main-nav{position:absolute;top:26px;left:697px;display:flex;font-family:"Montserrat",sans-serif;font-size:10.5px;color:var(--ink)}
.main-nav a{color:inherit;text-decoration:none;line-height:18px;height:20px;padding:0 8px;border:1px solid transparent}
.main-nav a.active{color:var(--accent);border-color:var(--accent);border-radius:2px}
.main-nav a+a{margin-left:14px}
.intro-band{position:absolute;left:0;top:344px;width:1200px;height:151px;background:var(--band);text-align:center}
.tagline{position:absolute;top:22px;left:0;width:100%;font-size:33px;font-weight:700;color:var(--ink);letter-spacing:.5px}
.tagline span{color:var(--accent)}
.tagline-rule{position:absolute;top:41px;height:2px;background:var(--accent)}
.tagline-rule.left{left:0;width:370px}
.tagline-rule.right{left:827px;width:373px}
.intro-text{position:absolute;top:86px;left:230px;width:740px;font-size:20.5px;font-weight:600;line-height:23px;color:var(--ink)}
.emphasis{position:absolute;top:574px;left:0;width:1200px;text-align:center}
.emphasis h2{font-size:20.5px;font-weight:700;color:var(--ink)}
.emphasis h2 span{color:var(--accent)}
.emphasis p{width:710px;margin:0 auto;font-size:12.4px;line-height:19.2px}
.emphasis h2+p{margin-top:21px}
.emphasis p+p{margin-top:24px}
.hl{color:var(--accent)}
.divider{position:absolute;left:216px;top:783px;width:768px;border-top:1px dashed var(--rule)}
.history{position:absolute;left:237px;top:823px;width:730px;font-family:"Noto Serif",Georgia,serif;font-size:11.8px;line-height:19.2px;color:var(--body)}
.history p+p{margin-top:24px}
.site-footer{position:absolute;left:0;top:1057px;width:1200px;height:143px;background:var(--footer-bg);color:#fff;text-align:center;font-size:10.3px;font-weight:700}
.site-footer .address{margin-top:36px;line-height:17px}
.site-footer .legal{margin-top:28px;word-spacing:1px}
</style>
</head>
<body>
<div class="hero" role="img" aria-label="Photograph of a city skyline at dusk beside a lake, lights glowing under a cloudy sky"></div>

<header class="site-header">
  <div class="brand"><span class="brand-mark"></span>PVT LAW GROUP PLLC</div>
  <nav class="main-nav">
    <a class="active" href="#">HOME</a>
    <a href="#">EXPERIENCE</a>
    <a href="#">ABOUT</a>
    <a href="#">CONTACT</a>
  </nav>
</header>

<section class="intro-band">
  <div class="tagline-rule left"></div>
  <div class="tagline-rule right"></div>
  <h1 class="tagline">IMAGINE<span>,</span> SECURE<span>,</span> PROTECT</h1>
  <p class="intro-text">PVT Law Group enjoys providing proactive, business-minded, efficient legal solutions for individuals and companies that benefit from major law firm</p>
</section>

<section class="emphasis">
  <h2>Some <span>areas of emphasis</span> include:</h2>
  <p><span class="hl">Counseling individuals and companies</span> with respect to clearing, selecting, securing, managing, commercializing, and protecting intellectual property assets around the world. This includes traditional global brand management, marketing, advertising, and enforcement work as well as litigation.</p>
  <p>PVT Law Group also provides <span class="hl">general counseling services for individuals and businesses</span>, from start-up advice to sophisticated business transactions strategy, agreement negotiating, dispute resolution, and litigation.</p>
</section>

<div class="divider"></div>

<section class="history">
  <p><span class="hl">Before founding PVT Law Group in 2008, Curtis L. Abernathy led the Trademark, Copyright, &amp; Brand Management Group for Falkner &amp; Ingleby's Seattle office</span>. Curtis was also a senior associate at Silicon Valley based Hartwell, Bexley, Oduya, &amp; Penrose.</p>
  <p>Over the years, Curtis has worked with start-ups to Global 25 corporations spanning various industries and continues to team with legal professionals in the U.S. and abroad to best serve his clients' needs.</p>
  <p>For example, PVT Law Group recently successfully enforced a company's branding rights in Europe while obtaining an order of costs in the company's favor. Curtis is also working on trademark filing programs for companies using the Madrid Protocol as well as national applications in jurisdictions all over the world, including Africa, Canada, the European Union, and Mexico</p>
</section>

<footer class="site-footer">
  <p class="address">427 W. ELMCREST AVE. SUITE C. SEATTLE WA. 98107<br>TEL: 206.555.0142 | FAX: 206.555.0143</p>
  <p class="legal">© 2008-2017 PVT LAW GROUP PLLC &nbsp; | &nbsp; All Rights Reserved &nbsp; | &nbsp; contact@pvtlegalhouse.com</p>
</footer>
</body>
</html>
```